Venture Capital and Sales/Marketing Consultancy Business Needs a Wordpress Design

I need a new web site design to replace our current site built based on Wordpress. Existing hostarvel wordpress hosting can be used. Completely new design, new content and new features can be added. This is a web site for information purposes ONLY. My company offer consulting services to start up or high growth technology companies to help them with financing (venture Capital or angel investment) and marketing/sales/product management expertise. We focus on driving growth through our access to venture capitals and business development strategies. We've helped many start up companies in the past - through my consulting business operating under my name. Now I have turned this business into an organization offering not only sales/marketing expertise but also investment support to help those start up companies.

Target Market(s)

Early Stage Technology Start-ups, Technology Companies with independent intellectual properties. Venture Capital and investment companies looking into technology investment. Companies looking into market expansions in North America and APAC especially China). Product seeking business development partners to reduce marketing and operational risk in developing North American and APAC markets. Technologies demanding Intellectual Property protection in North American and Chinese market.

Industry/Entity Type

Investment

Font styles to use
Sans Serif

Colors
ffcf3e

Requirements
Must have
• Basic features such as Newsfeeds to News page.
• Following pages are required: About Us, Projects, Partners and Contact Us
• Designer will also help with:
• Implementing the design into the current wordpress account hosted by hostarvel.
• All Graphics used in the design need to be included.
Nice to have
• A proposal submission page allow submission of project proposal in PDF format only. Files submitted can be automatically forwarded to an email alias.

```html
<!DOCTYPE html>
<html lang="en">
<head>
<meta charset="utf-8">
<title>Corvania — Venture Capital &amp; Marketing Consultancy</title>
<link rel="stylesheet" href="https://fonts.googleapis.com/css2?family=Open+Sans:wght@400;600;700&family=Arimo:wght@400;700&display=swap">
<style>
:root{
  --gold:#ffcf3e;
  --ink:#222222;
  --text:#555555;
  --bar:#1f1f1f;
  --header-top:#343434;
  --header-bottom:#181818;
  --light:#f3f3f3;
  --news:#e6e6e6;
  --footer:#2b2b2b;
  --muted:#9a9a9a;
  --line:#cfcfcf;
}
*{box-sizing:border-box;margin:0;padding:0}
html,body{width:1200px;height:2375px;overflow:hidden}
body{position:relative;background:#fff;font-family:"Arimo",Arial,sans-serif;color:var(--text)}
.abs{position:absolute}
.heading{font-family:"Open Sans",Arial,sans-serif;font-weight:700;color:var(--ink);text-transform:uppercase}
.center{text-align:center}

/* top bar */
.topbar{left:0;top:0;width:1200px;height:41px;background:var(--bar);color:#cfcfcf;font-family:"Open Sans",sans-serif;font-size:12px}
.topbar .contact{left:98px;top:13px;display:flex;gap:28px;align-items:center}
.topbar .contact span{display:flex;align-items:center;gap:8px}
.topbar .follow{right:98px;top:13px;display:flex;gap:16px;align-items:center}
.dot{width:10px;height:10px;border-radius:50%;background:#8a8a8a;display:inline-block}

/* header */
.header{left:0;top:41px;width:1200px;height:98px;background:linear-gradient(var(--header-top),var(--header-bottom))}
.brand{left:98px;top:18px;width:80px;display:flex;flex-direction:column;align-items:center;gap:6px}
.brand .mark{width:34px;height:34px;border-radius:50%;background:var(--gold)}
.brand .name{font-family:"Open Sans",sans-serif;font-weight:700;font-size:12px;color:var(--gold);letter-spacing:.5px}
.nav{top:41px;font-family:"Open Sans",sans-serif;font-size:12px;color:#fff;text-transform:uppercase}
.nav a{position:absolute;color:#fff;text-decoration:none;white-space:nowrap}

/* hero */
.hero{left:0;top:139px;width:1200px;height:483px;background:linear-gradient(180deg,#6b5a48 0%,#b5773d 35%,#5a4a3e 60%,#2d2a2a 100%)}
.hero h1{position:absolute;left:0;width:1200px;top:228px;font-family:"Open Sans",sans-serif;font-weight:700;font-size:30px;color:#fff;text-align:center}
.hero p{position:absolute;left:175px;width:850px;top:278px;font-family:"Open Sans",sans-serif;font-size:16px;line-height:30px;color:#fff;text-align:center;text-transform:uppercase}
.hero .arrow{position:absolute;top:205px}

/* welcome */
.welcome{left:0;top:622px;width:1200px;height:435px;background:var(--light)}
.section-title{position:absolute;left:0;width:1200px;font-size:22px}
.lead{position:absolute;left:180px;width:840px;font-size:11.5px;line-height:23px;text-align:center;color:#555}
.feature{position:absolute;width:300px;text-align:center}
.feature .icon{width:70px;height:70px;border:2px solid #9a9a9a;border-radius:50%;margin:0 auto;display:flex;align-items:center;justify-content:center;background:#fff}
.feature h3{font-size:14px;margin-top:34px}
.feature p{font-size:11.5px;line-height:23px;margin-top:12px;padding:0 22px}

/* about */
.about{left:0;top:1057px;width:1200px;height:325px;background:linear-gradient(90deg,#1c2a3a 0%,#3b4a5a 45%,#2c3744 75%,#141d29 100%)}
.about .section-title{color:#fff;top:70px}
.about .lead{color:#fff;top:116px}
.btn{position:absolute;left:507px;top:214px;width:186px;height:46px;border:2px solid #fff;color:#fff;font-family:"Open Sans",sans-serif;font-weight:700;font-size:12px;display:flex;align-items:center;justify-content:center;text-transform:uppercase}

/* projects */
.projects{left:0;top:1382px;width:1200px;height:396px;background:var(--light)}
.projects .intro{position:absolute;left:128px;width:288px;text-align:right}
.projects .intro h2{font-size:22px;margin-top:70px;line-height:30px}
.projects .intro .sub{font-size:13px;line-height:22px;color:#222;margin-top:12px}
.projects .intro .body{font-size:11.5px;line-height:21px;margin-top:10px}
.pager{position:absolute;left:364px;top:302px;display:flex;gap:2px}
.pager span{width:24px;height:24px;background:#c8c8c8;display:flex;align-items:center;justify-content:center}
.card{position:absolute;top:71px;width:293px}
.card .photo{width:293px;height:163px}
.card h3{font-size:13px;line-height:24px;margin-top:21px}
.card p{font-size:11.5px;line-height:23px;margin-top:9px}

/* news */
.news{left:0;top:1778px;width:1200px;height:402px;background:var(--news)}
.news .section-title{top:42px}
.news .lead{top:84px}
.post-photo{left:168px;top:160px;width:272px;height:175px;background:linear-gradient(135deg,#dfe4ea,#8a93a0 55%,#2d2f35)}
.post{left:480px;top:162px;width:590px}
.post h3{font-size:13px}
.post .date{font-size:13px;color:#444;margin-top:12px}
.post p{font-size:11.5px;line-height:22px;margin-top:10px}
.news .arrow{position:absolute;top:232px}

/* partners */
.partners{left:0;top:2180px;width:1200px;height:92px;background:#fff;display:flex;justify-content:center;align-items:center;gap:52px}
.partner{height:36px;background:#c9c9c9;border-radius:4px}

/* footer */
.footer{left:0;top:2272px;width:1200px;height:103px;background:var(--footer);font-family:"Open Sans",sans-serif;color:#bbbbbb}
.footer .brand{top:20px}
.footer .brand .mark{background:#777}
.footer .brand .name{color:#9a9a9a}
.footer-nav{left:193px;top:30px;font-size:10px;display:flex;gap:14px;text-transform:uppercase}
.copy{left:193px;top:60px;font-size:9px;color:var(--muted);text-transform:uppercase}
.social{right:148px;top:36px;display:flex;align-items:center;gap:10px;font-size:10px;text-transform:uppercase}
.social .ring{width:32px;height:32px;border:1px solid #777;border-radius:50%}
</style>
</head>
<body>

<div class="abs topbar">
  <div class="abs contact">
    <span><svg width="8" height="12" viewBox="0 0 8 12"><rect x="0.5" y="0.5" width="7" height="11" rx="1.5" fill="none" stroke="#cfcfcf"/><circle cx="4" cy="9.5" r="0.8" fill="#cfcfcf"/></svg>CALL US : (2365) 418 902</span>
    <span><svg width="12" height="9" viewBox="0 0 12 9"><rect x="0.5" y="0.5" width="11" height="8" fill="#cfcfcf"/><path d="M0.5 0.5 6 5 11.5 0.5" fill="none" stroke="#1f1f1f"/></svg>EMAIL US : info@corvania.com</span>
  </div>
  <div class="abs follow">FOLLOW US :
    <i class="dot"></i><i class="dot"></i><i class="dot"></i><i class="dot"></i><i class="dot"></i>
  </div>
</div>

<header class="abs header">
  <div class="abs brand"><div class="mark"></div><div class="name">CORVANIA</div></div>
  <nav class="abs nav" style="left:0;width:1200px">
    <a style="left:537px">Home</a>
    <a style="left:642px">About Us</a>
    <a style="left:769px">Projects</a>
    <a style="left:892px">Partners</a>
    <a style="left:1019px">Contact Us</a>
  </nav>
</header>

<section class="abs hero" role="img" aria-label="Photograph of a city skyline with a tall skyscraper at sunset">
  <svg class="arrow" style="left:44px" width="16" height="60" viewBox="0 0 16 60"><path d="M14 2 2 30 14 58" fill="none" stroke="rgba(255,255,255,.5)" stroke-width="1.5"/></svg>
  <svg class="arrow" style="left:1140px" width="16" height="60" viewBox="0 0 16 60"><path d="M2 2 14 30 2 58" fill="none" stroke="rgba(255,255,255,.5)" stroke-width="1.5"/></svg>
  <h1>VENTURE CAPITAL &amp; MARKETING CONSULTANCY</h1>
  <p>We help venture capital and investment companies looking into technology investment. Companies looking into market expansions in North America and APAC especially China.</p>
</section>

<section class="abs welcome">
  <h2 class="heading section-title center" style="top:46px">Welcome to Corvania</h2>
  <p class="lead" style="top:86px">Lorem Ipsum is simply dummy text of the printing and typesetting industry. Lorem Ipsum has been the industry's standard dummy text ever since the 1500s, when an unknown printer took a galley of type and scrambled it to make a type specimen book. It has survived not only five centuries, but also the leap into electronic typesetting, remaining essentially unchanged</p>

  <div class="feature" style="left:106px;top:193px">
    <div class="icon"><svg width="30" height="26" viewBox="0 0 30 26"><path d="M1 1v24h28" fill="none" stroke="#777" stroke-width="2"/><rect x="6" y="14" width="3" height="8" fill="#777"/><rect x="11" y="8" width="3" height="14" fill="#777"/><rect x="16" y="11" width="3" height="11" fill="#777"/><rect x="21" y="6" width="3" height="16" fill="#777"/></svg></div>
    <h3 class="heading">Simplemente el texto de</h3>
    <p>Lorem Ipsum is simply dummy text of the printing and typesetting industry. Lorem Ipsum has been the industry's standard dummy...</p>
  </div>
  <div class="feature" style="left:442px;top:193px">
    <div class="icon"><svg width="24" height="30" viewBox="0 0 24 30"><rect x="1" y="1" width="22" height="28" rx="2" fill="none" stroke="#777" stroke-width="2"/><rect x="5" y="5" width="14" height="5" fill="#777"/><g fill="#777"><rect x="5" y="13" width="3" height="3"/><rect x="10.5" y="13" width="3" height="3"/><rect x="16" y="13" width="3" height="3"/><rect x="5" y="18" width="3" height="3"/><rect x="10.5" y="18" width="3" height="3"/><rect x="16" y="18" width="3" height="3"/><rect x="5" y="23" width="3" height="3"/><rect x="10.5" y="23" width="3" height="3"/><rect x="16" y="23" width="3" height="3"/></g></svg></div>
    <h3 class="heading">Simplemente el texto de</h3>
    <p>Lorem Ipsum is simply dummy text of the printing and typesetting industry. Lorem Ipsum has been the industry's standard dummy...</p>
  </div>
  <div class="feature" style="left:793px;top:193px">
    <div class="icon"><svg width="32" height="30" viewBox="0 0 32 30"><circle cx="12" cy="17" r="7" fill="none" stroke="#777" stroke-width="5" stroke-dasharray="3 2.5"/><circle cx="12" cy="17" r="3" fill="#777"/><circle cx="24" cy="8" r="4.5" fill="none" stroke="#777" stroke-width="3.5" stroke-dasharray="2 2"/><circle cx="25" cy="23" r="3.5" fill="none" stroke="#777" stroke-width="3" stroke-dasharray="2 1.6"/></svg></div>
    <h3 class="heading">Simplemente el texto de</h3>
    <p>Lorem Ipsum is simply dummy text of the printing and typesetting industry. Lorem Ipsum has been the industry's standard dummy...</p>
  </div>
</section>

<section class="abs about" role="img" aria-label="Photograph of two businessmen in suits in a meeting, darkened">
  <h2 class="heading section-title center">About Corvania</h2>
  <p class="lead">Lorem Ipsum is simply dummy text of the printing and typesetting industry. Lorem Ipsum has been the industry's standard dummy text ever since the 1500s, when an unknown printer took a galley of type and scrambled it to make a type specimen book. It has survived not only five centuries, but also the leap into electronic typesetting, remaining essentially unchanged</p>
  <div class="btn">Read more info</div>
</section>

<section class="abs projects">
  <div class="intro">
    <h2 class="heading">Corvania Projects</h2>
    <p class="sub">Lorem Ipsum is simply dummy text of the printing and typesetting industry</p>
    <p class="body">Lorem Ipsum is simply dummy text of the printing and typesetting industry. Lorem Ipsum has been the industry's standard dummy text ever since the 1500s, when an unknown printer took a galley of type and scrambled it to make a type specimen book.</p>
  </div>
  <div class="pager">
    <span><svg width="8" height="10" viewBox="0 0 8 10"><path d="M6 1 2 5 6 9" fill="none" stroke="#fff" stroke-width="1.5"/></svg></span>
    <span><svg width="8" height="10" viewBox="0 0 8 10"><path d="M2 1 6 5 2 9" fill="none" stroke="#fff" stroke-width="1.5"/></svg></span>
  </div>
  <article class="card" style="left:476px">
    <div class="photo" role="img" aria-label="Photograph of hands holding a wall clock against a blue cloudy sky" style="background:linear-gradient(160deg,#6f9fd3,#b7cde6 50%,#3f6ea8)"></div>
    <h3 class="heading">Lorem Ipsum es simplemente el texto de relleno de las imprentas</h3>
    <p>Lorem Ipsum is simply dummy text of the printing and typesetting industry. Lorem Ipsum has been the industry's standard dummy...</p>
  </article>
  <article class="card" style="left:809px">
    <div class="photo" role="img" aria-label="Photograph of a man with a laptop sitting in a busy crowd" style="background:linear-gradient(160deg,#9aa3ad,#5d636b 55%,#3a3f46)"></div>
    <h3 class="heading">Lorem Ipsum es simplemente el texto de relleno de las imprentas</h3>
    <p>Lorem Ipsum is simply dummy text of the printing and typesetting industry. Lorem Ipsum has been the industry's standard dummy...</p>
  </article>
</section>

<section class="abs news">
  <h2 class="heading section-title center">Latest News</h2>
  <p class="lead">Lorem Ipsum is simply dummy text of the printing and typesetting industry. Lorem Ipsum has been the industry's standard dummy text ever since the 1500s, when an unknown printer took a galley of type and scrambled it to make a type specimen book.</p>
  <svg class="arrow" style="left:106px" width="12" height="36" viewBox="0 0 12 36"><path d="M10 2 2 18 10 34" fill="none" stroke="#aaa" stroke-width="1.5"/></svg>
  <svg class="arrow" style="left:1094px" width="12" height="36" viewBox="0 0 12 36"><path d="M2 2 10 18 2 34" fill="none" stroke="#aaa" stroke-width="1.5"/></svg>
  <div class="abs post-photo" role="img" aria-label="Photograph of two business colleagues reviewing documents at a desk"></div>
  <article class="abs post">
    <h3 class="heading">Lorem Ipsum es simplemente el texto de relleno de las...</h3>
    <p class="date">Posted on 27 March 2014</p>
    <p>Lorem Ipsum es simplemente el texto de relleno de las imprentas y archivos de texto. Lorem Ipsum ha sido el texto de relleno estándar de las industrias desde el año 1500, cuando un impresor (N. del T. persona que se dedica a la imprenta) desconocido usó una galería de textos y los mezcló de tal manera que logró hacer un libro de textos especimen.No sólo sobrevivió 500 años, sino que tambien ingresó como texto de relleno en documentos electrónicos, quedando esencialmente igual al original.</p>
  </article>
</section>

<section class="abs partners" aria-label="Partners">
  <div class="partner" style="width:140px"></div>
  <div class="partner" style="width:150px"></div>
  <div class="partner" style="width:132px"></div>
  <div class="partner" style="width:134px"></div>
  <div class="partner" style="width:80px"></div>
  <div class="partner" style="width:106px"></div>
</section>

<footer class="abs footer">
  <div class="abs brand"><div class="mark"></div><div class="name">CORVANIA</div></div>
  <div class="abs footer-nav"><span>Home</span><span>/</span><span>About Us</span><span>/</span><span>Projects</span><span>/</span><span>Partners</span><span>/</span><span>Contact Us</span></div>
  <div class="abs copy">© 2014. Corvania. All rights reserved.</div>
  <div class="abs social">Connect with our social network :
    <i class="ring"></i><i class="ring"></i><i class="ring"></i><i class="ring"></i><i class="ring"></i>
  </div>
</footer>

</body>
</html>
```